Tess Marlowe Communication business card

I am starting a small, country-based business that offers writing, communication and marketing services to a wide range of clients, inner city big business, to mining, through to agriculture.

The appeal of my business is that it's mobile and flexible. It's just me, with lots of hands-on experience on construction and infrastructure projects.

I can provide the following services:

• Communication planning and management
• Issues and media management
• Marketing and communication materials
• Project management and strategy
• Government liaison
• Incident management communication
• Stakeholder management

It would be great to be able to use the elements of the business card design on other stationery.

Industry/Entity Type

Communication

Requirements
Must have
• The following information:

Tess Marlowe
M: 0427 391 864
E: tess@tmcommsmail.com

PO Box 152
Durrandale Q 4472
Nice to have
• a rural element (windmill, workboots, wheat stalk)

```html
<!DOCTYPE html>
<html lang="en">
<head>
<meta charset="utf-8">
<title>Tess Marlowe Communication – Stationery</title>
<link href="https://fonts.googleapis.com/css2?family=Exo+2:wght@300;400;600;700&family=Nunito+Sans:wght@400&display=swap" rel="stylesheet">
<style>
  :root {
    --slate: #2e4657;
    --mist: #8aa8b8;
    --ink: #4b5a66;
    --field: #7a9444;
    --field-dark: #5f7a35;
    --paper: #ffffff;
    --board-light: #f2f4f4;
    --board-dark: #b9bfc1;
    --label: #1e1e1e;
  }
  * { margin: 0; padding: 0; box-sizing: border-box; }
  html, body { width: 1200px; height: 900px; overflow: hidden; }
  body {
    position: relative;
    background: radial-gradient(ellipse at 45% 40%, var(--board-light) 0%, #dfe3e4 45%, var(--board-dark) 100%);
    font-family: "Exo 2", sans-serif;
  }
  .sheet {
    position: absolute;
    background: var(--paper);
    box-shadow: 4px 6px 10px rgba(0, 0, 0, 0.35);
  }
  .view-label {
    position: absolute;
    font-family: "Nunito Sans", sans-serif;
    font-size: 26px;
    letter-spacing: 2px;
    color: var(--label);
  }

  /* Business card – front */
  .card-front { left: 40px; top: 44px; width: 613px; height: 394px; z-index: 2; }
  .card-front .wordmark {
    position: absolute; left: 43px; top: 88px; width: 535px;
    color: var(--slate); font-weight: 600;
  }
  .wordmark-name { display: block; font-size: 70px; line-height: 1; letter-spacing: 0.5px; }
  .wordmark-line { display: block; text-align: right; font-size: 36px; line-height: 1; margin-top: 14px; }
  .card-front .contact { position: absolute; left: 308px; top: 252px; color: var(--ink); }
  .contact-name { font-size: 19px; font-weight: 600; color: var(--mist); margin-bottom: 12px; }
  .contact-line { font-size: 19px; font-weight: 400; line-height: 26px; }

  /* Business card – back */
  .card-back {
    left: 286px; top: 424px; width: 464px; height: 298px; z-index: 1;
    background: linear-gradient(160deg, var(--field) 0%, var(--field-dark) 100%);
  }

  /* Headed paper */
  .letterhead { left: 674px; top: 141px; width: 491px; height: 694px; }
  .letterhead .wordmark { position: absolute; left: 42px; top: 28px; color: var(--slate); font-weight: 600; width: 322px; }
  .letterhead .wordmark-name { font-size: 42px; }
  .letterhead .wordmark-line { font-size: 21px; margin-top: 6px; }
  .letterhead-footer {
    position: absolute; left: 30px; right: 30px; top: 620px;
    display: flex; justify-content: space-between;
    font-size: 11px; color: var(--ink);
  }
  .letterhead-footer b { font-weight: 700; color: var(--slate); }
  .letterhead-band {
    position: absolute; left: 0; right: 0; bottom: 0; height: 55px;
    background: linear-gradient(90deg, var(--field) 0%, var(--field-dark) 100%);
  }
</style>
</head>
<body>
  <section class="sheet card-front">
    <div class="wordmark">
      <span class="wordmark-name">Tess Marlowe</span>
      <span class="wordmark-line">Communication</span>
    </div>
    <div class="contact">
      <p class="contact-name">Tess Marlowe</p>
      <p class="contact-line">0427 391 864</p>
      <p class="contact-line">tess@tmcommsmail.com</p>
      <p class="contact-line">PO Box 152, Durrandale Q 4472</p>
    </div>
  </section>
  <p class="view-label" style="left:42px; top:446px;">Front</p>

  <section class="sheet card-back" role="img" aria-label="Repeating pattern of white, dark green and navy wheat stalks on olive green"></section>
  <p class="view-label" style="left:288px; top:731px;">Back</p>

  <section class="sheet letterhead">
    <div class="wordmark">
      <span class="wordmark-name">Tess Marlowe</span>
      <span class="wordmark-line">Communication</span>
    </div>
    <div class="letterhead-footer">
      <span><b>M:</b> 0427 391 864</span>
      <span><b>E:</b> tess@tmcommsmail.com</span>
      <span>PO Box 152, Durrandale Q 4472</span>
    </div>
    <div class="letterhead-band" role="img" aria-label="Strip of wheat stalk pattern in white, dark green and navy on olive green"></div>
  </section>
  <p class="view-label" style="left:674px; top:845px;">Example of headed paper</p>
</body>
</html>
```